Commercial painting contractor in need of graphic designs for new trade show booth.

Brellow Holdings, Inc. is a leading commercial and multifamily painter in Texas for new construction interested in growing its repaint business. We will be attending the Lone Pecan Rental Housing Guild Expo in October and are looking to finalize our booth design and get it ordered by 8/15. The booth layout is selected, and we have a logo and basic brand board. We are looking for graphic design that we can use for the next 3+ years without appearing dated. We are considering incorporating more of the baby blue color into our repaint branding (see bh-logo-dark blued-bg attached). The blue and white logo is our standard.
BrellowCo website: www.coatworksvale.com
Trade Show booth website: https://quickexhibitframes.com/10X10-Custom-Trade-Show-Display-Booth-I

```html
<!DOCTYPE html>
<html lang="en">
<head>
<meta charset="utf-8">
<title>Brellow Holdings, Inc. — Booth Graphics</title>
<link href="https://fonts.googleapis.com/css2?family=Archivo:wght@700&display=swap" rel="stylesheet">
<style>
  :root {
    --navy: #1b2a55;
    --royal: #1b2185;
    --blue: #1f6fe0;
    --sky: #3fa3e0;
    --baby: #4cc3de;
    --fabric: #e7e8ea;
    --white: #ffffff;
    --page: #f2f3f5;
  }
  * { box-sizing: border-box; margin: 0; padding: 0; }
  html, body { width: 1200px; height: 1200px; overflow: hidden; background: var(--page); }
  .booth-sheet { position: relative; width: 1200px; height: 1200px; }
  .panel { position: absolute; overflow: hidden; }
  .panel svg { position: absolute; inset: 0; width: 100%; height: 100%; }

  .back-wall { left: 60px; top: 50px; width: 1080px; height: 600px; border-radius: 18px; background: var(--navy); }
  .back-wall .hero-photo {
    position: absolute; left: 380px; top: 0; width: 470px; height: 600px;
    background: linear-gradient(160deg, #e9e6e1 0%, #c9c3ba 45%, #6b7fa6 70%, #2b3f78 100%);
  }

  .tower { left: 60px; top: 690px; width: 260px; height: 470px; }
  .tower-header {
    position: absolute; left: 0; top: 0; width: 260px; height: 170px;
    border-radius: 130px 130px 0 0;
    background: radial-gradient(circle at 50% 30%, #27309a, var(--royal) 70%);
    display: flex; align-items: flex-end; justify-content: center; padding-bottom: 34px;
  }
  .tower-body { position: absolute; left: 30px; top: 170px; width: 200px; height: 300px; background: var(--fabric); overflow: hidden; }

  .brand-name {
    font-family: "Archivo", Arial, sans-serif; font-weight: 700; font-style: normal;
    letter-spacing: 0.2px; white-space: nowrap; text-align: center;
  }
  .tower-header .brand-name { color: var(--white); font-size: 15px; }

  .kiosk { left: 370px; top: 690px; width: 190px; height: 470px; border-radius: 40px 40px 8px 8px; background: var(--white); }
  .kiosk .brand-name { position: absolute; top: 155px; width: 100%; color: var(--royal); font-size: 11px; }

  .counter { left: 610px; top: 760px; width: 530px; height: 400px; border-radius: 8px; background: var(--fabric); }
  .counter .brand-name { position: absolute; top: 140px; width: 100%; color: var(--royal); font-size: 30px; }
</style>
</head>
<body>
<main class="booth-sheet">

  <section class="panel back-wall" aria-label="Back wall graphic">
    <div class="hero-photo" role="img" aria-label="Photo of a painter in cap and overalls rolling paint onto a white wall"></div>
    <svg viewBox="0 0 1080 600" preserveAspectRatio="none">
      <path d="M1080 0 L1040 0 C960 150 900 380 860 600 L1080 600 Z" fill="var(--navy)"/>
      <path d="M1030 0 L1005 0 C930 170 880 400 850 600 L872 600 C905 400 960 180 1030 0 Z" fill="var(--sky)"/>
      <path d="M1080 60 C990 220 935 420 910 600 L935 600 C965 420 1010 260 1080 130 Z" fill="var(--blue)"/>
      <path d="M1080 180 C1020 310 985 450 968 600 L985 600 C1005 460 1040 330 1080 230 Z" fill="var(--baby)"/>
      <path d="M1080 300 C1000 360 960 470 950 600 L1080 600 Z" fill="#0f1a3d"/>
      <path d="M0 600 C40 520 70 470 110 430 L110 600 Z" fill="var(--baby)"/>
    </svg>
  </section>

  <section class="panel tower" aria-label="Monitor tower graphic">
    <div class="tower-header">
      <p class="brand-name">BRELLOW HOLDINGS, INC.</p>
    </div>
    <div class="tower-body">
      <svg viewBox="0 0 200 300" preserveAspectRatio="none">
        <path d="M0 0 C40 80 90 180 140 300 L0 300 Z" fill="var(--navy)"/>
        <path d="M10 0 C50 90 110 190 150 300 L175 300 C130 190 60 80 10 0 Z" fill="var(--blue)"/>
        <path d="M30 0 C80 90 140 200 180 300 L195 300 C150 200 90 90 30 0 Z" fill="var(--sky)"/>
      </svg>
    </div>
  </section>

  <section class="panel kiosk" aria-label="Tablet kiosk graphic">
    <p class="brand-name">BRELLOW HOLDINGS, INC.</p>
    <svg viewBox="0 0 190 470" preserveAspectRatio="none">
      <path d="M0 300 C70 300 140 330 190 380 L190 470 L0 470 Z" fill="var(--navy)"/>
      <path d="M0 285 C80 285 150 320 190 360 L190 380 C140 335 70 305 0 305 Z" fill="var(--sky)"/>
      <path d="M0 340 C50 345 100 370 130 400 C90 380 45 365 0 360 Z" fill="var(--blue)"/>
    </svg>
  </section>

  <section class="panel counter" aria-label="Counter wrap graphic">
    <p class="brand-name">BRELLOW HOLDINGS, INC.</p>
    <svg viewBox="0 0 530 400" preserveAspectRatio="none">
      <path d="M0 300 C180 270 380 270 530 310 L530 400 L0 400 Z" fill="var(--navy)"/>
      <path d="M0 280 C180 250 380 255 530 295 L530 312 C380 275 180 272 0 302 Z" fill="var(--blue)"/>
      <path d="M0 268 C180 240 380 245 530 285 L530 296 C380 258 180 253 0 282 Z" fill="var(--sky)"/>
      <path d="M300 325 C400 320 480 340 530 370 L530 390 C470 355 390 335 300 325 Z" fill="var(--baby)"/>
    </svg>
  </section>

</main>
</body>
</html>
```